International Reinsurance Business Platform Needs a PowerPoint Design

We need a powerpoint design for a new company based in Bermuda. We have created a platform to facilitate the incorporation and creation of off-shore reinsurance companies, primarily offered to asset managers to generate permanent capital at a fraction of the costs typically required by such a venture. We have no preference as to the color scheme, but would like for the final design to communicate professionalism, simplicity and elegance.
We have uploaded a very rudimentary draft (far from what we want), and welcome you to recreate a single page from it (it can be a combination of two pages into one; preferably something complicated enough to showcase the potential of your idea). From there, we will pick from the better submissions (of that single page) and work from there.
Target Market(s)
High-income asset managers
Industry/Entity Type
Business

```html
<!DOCTYPE html>
<html lang="en">
<head>
<meta charset="utf-8">
<title>Tessera Re – Slide Concepts</title>
<link rel="stylesheet" href="https://fonts.googleapis.com/css2?family=Fira+Sans:wght@400;600&display=swap">
<style>
  :root {
    --green: #009a44;
    --green-mid: #4cb37a;
    --green-light: #9fd2b2;
    --ink: #3c3c3c;
    --muted: #7a7a7a;
    --rule: #b9bcb9;
    --page: #ffffff;
    --slide-top: #eef0ee;
    --slide-bottom: #e9ebe9;
  }
  * { box-sizing: border-box; margin: 0; padding: 0; }
  html, body { width: 1200px; height: 1000px; overflow: hidden; background: var(--page); }
  body { position: relative; font-family: "Fira Sans", sans-serif; color: var(--ink); }

  .sheet-label {
    position: absolute; left: 183px; top: 115px;
    font-size: 19px; letter-spacing: 0.5px; color: #111;
  }

  .slide {
    position: absolute; width: 414px; height: 312px;
    background: linear-gradient(180deg, var(--slide-top) 0%, #fafbfa 30%, #ffffff 55%, #f7f8f7 80%, var(--slide-bottom) 100%);
    box-shadow: 0 0 0 1px #eceeec;
  }
  .slide--one { left: 173px; top: 168px; }
  .slide--two { left: 611px; top: 168px; }
  .slide--three { left: 173px; top: 502px; }
  .slide--four { left: 611px; top: 502px; }

  .slide__bar { position: absolute; top: 0; left: 0; width: 385px; height: 11px; background: var(--green); }
  .slide__chip { position: absolute; top: 0; height: 11px; }
  .slide__chip--mid { left: 388px; width: 12px; background: var(--green-mid); }
  .slide__chip--light { left: 403px; width: 9px; background: var(--green-light); }

  .slide__title {
    position: absolute; left: 39px; top: 42px;
    font-size: 16.5px; font-weight: 400; color: var(--green);
  }
  .slide__heading {
    position: absolute; left: 40px;
    font-size: 9.5px; font-weight: 600; color: var(--green); letter-spacing: 0.2px;
  }
  .bullets { position: absolute; left: 40px; list-style: none; font-size: 8.6px; }
  .bullets li { height: 18px; line-height: 18px; white-space: nowrap; }
  .bullets li::before { content: "•"; margin-right: 4px; }
  .bullets--sub { left: 61px; }
  .bullets--sub li::before { content: "-"; margin-right: 5px; }

  .slide__rule { position: absolute; left: 39px; top: 268px; width: 252px; height: 1px; background: var(--rule); }
  .slide__footer {
    position: absolute; left: 40px; top: 284px;
    font-size: 5.6px; color: var(--muted); white-space: nowrap; word-spacing: 0.5px;
  }
  .slide__footer .sep { margin: 0 7px; }

  .brand-mark {
    position: absolute; left: 300px; top: 263px;
    display: flex; align-items: center; gap: 5px;
    font-size: 8px; font-weight: 600; color: var(--green); white-space: nowrap;
  }
  .brand-mark__dot { width: 10px; height: 10px; border-radius: 50%; background: var(--green); }
</style>
</head>
<body>

<div class="sheet-label">FONT: HUMANIST SANS, SLIDE: 3,4,5</div>

<section class="slide slide--one">
  <div class="slide__bar"></div><div class="slide__chip slide__chip--mid"></div><div class="slide__chip slide__chip--light"></div>
  <h2 class="slide__heading" style="top:71px">EACH FACED SIGNIFICANT HURDLES</h2>
  <ul class="bullets" style="top:99px">
    <li>Had to hire marquee reinsurance teams</li>
    <li>Reinsurace teams received large guarantees</li>
    <li>Had to raise at least $250 million of capital</li>
    <li>Large busted deal, startup, and fixed costs</li>
    <li>Redirection of resources for 1 to 2 years</li>
  </ul>
  <h2 class="slide__heading" style="top:205px">MANY MORE HAVE TRIED AND FAILED</h2>
  <div class="slide__rule"></div>
  <div class="brand-mark"><span class="brand-mark__dot"></span>HALVARD CAPITAL</div>
  <p class="slide__footer">Martin R. Halvard<span class="sep">|</span>+41 70 555 01 23<span class="sep">|</span>mhalvard@halvardcapital.com<span class="sep">|</span>www.halvardcapital.com</p>
</section>

<section class="slide slide--two">
  <div class="slide__bar"></div><div class="slide__chip slide__chip--mid"></div><div class="slide__chip slide__chip--light"></div>
  <h2 class="slide__heading" style="top:71px">DESPITE HURDLES, BENEFITS ARE WORTH IT</h2>
  <ul class="bullets" style="top:99px">
    <li>Marlow model for outperformance (see QVR)</li>
    <li>Major increase in AuM from new sources</li>
    <li>All capital is permanent</li>
    <li>Better liquidity if publicly traded (see GLRX)</li>
    <li>Tax efficient (no K-1s, capital gains treatment)</li>
  </ul>
  <div class="slide__rule"></div>
  <div class="brand-mark"><span class="brand-mark__dot"></span>HALVARD CAPITAL</div>
  <p class="slide__footer">Martin R. Halvard<span class="sep">|</span>+41 70 555 01 23<span class="sep">|</span>mhalvard@halvardcapital.com<span class="sep">|</span>www.halvardcapital.com</p>
</section>

<section class="slide slide--three">
  <div class="slide__bar"></div><div class="slide__chip slide__chip--mid"></div><div class="slide__chip slide__chip--light"></div>
  <h1 class="slide__title">Tessera Re</h1>
  <h2 class="slide__heading" style="top:83px">ALL OF THE BENEFITS WITHOUT THE HURDLES</h2>
  <ul class="bullets" style="top:109px">
    <li>As little as 1% of the capital ($2+ million vs $250+ million)</li>
    <li>Minimal busted deal risk (maximum of $25k)</li>
    <li>Less than 10% of the startup costs ($100k vs $1+ million)</li>
    <li>Less than 5% of the fixed costs ($100k/yr vs $2+ mil/yr)</li>
    <li>No mgt comp guarantees (have been as high as $25 million)</li>
    <li>Speed to market (60 to 90 days vs. 1 to 2 years)</li>
  </ul>
  <div class="slide__rule"></div>
  <div class="brand-mark"><span class="brand-mark__dot"></span>HALVARD CAPITAL</div>
  <p class="slide__footer">Martin R. Halvard<span class="sep">|</span>+41 70 555 01 23<span class="sep">|</span>mhalvard@halvardcapital.com<span class="sep">|</span>www.halvardcapital.com</p>
</section>

<section class="slide slide--four">
  <div class="slide__bar"></div><div class="slide__chip slide__chip--mid"></div><div class="slide__chip slide__chip--light"></div>
  <h1 class="slide__title">Tessera Re</h1>
  <ul class="bullets" style="top:80px; font-size:9.2px">
    <li>All Tessera compensation is performance based</li>
  </ul>
  <ul class="bullets bullets--sub" style="top:104px">
    <li>Managing the entire business – 5% warrants</li>
    <li>Underwriting – 2% of increase in float paid by reinsurer</li>
    <li>Underwriting performance fee – 1/3rd cost of float under 3%/yr</li>
    <li>Monitor, renewals, claims – 20% of fees on float paid by asset mgr</li>
    <li>Capital raising from new investors – 3% of capital raised</li>
  </ul>
  <ul class="bullets" style="top:213px; font-size:9.2px">
    <li>Virtually no impact on growing or managing existing funds</li>
  </ul>
  <div class="slide__rule"></div>
  <div class="brand-mark"><span class="brand-mark__dot"></span>HALVARD CAPITAL</div>
  <p class="slide__footer">Martin R. Halvard<span class="sep">|</span>+41 70 555 01 23<span class="sep">|</span>mhalvard@halvardcapital.com<span class="sep">|</span>www.halvardcapital.com</p>
</section>

</body>
</html>
```